Need Business Card for our Real Estate Business with Sales Executive's Picture

PANTONE 484 C ( RED)

PANTONE 2766 C ( BLUE

Industry/Entity Type

Real Estate

Contact Information for Business Card

Name, Mobile, email, & picture of Person
Agency Phone, address, Web address

Requirements
Must have
• Our Logo Colours, Agent Picture,

```html
<!DOCTYPE html>
<html lang="en">
<head>
<meta charset="utf-8">
<title>Meridian Realty – Business Card</title>
<link rel="stylesheet" href="https://fonts.googleapis.com/css2?family=Roboto:wght@400;500;700&display=swap">
<style>
  :root {
    --navy: #0b1538;
    --accent-red: #8b1a1a;
    --paper: #f4f4f4;
    --ink: #4d4d4d;
    --white: #ffffff;
    --backdrop: #e9e6e1;
    --portrait-top: #2a3f7a;
    --portrait-bottom: #1a2a5c;
  }
  * { box-sizing: border-box; margin: 0; padding: 0; }
  html, body {
    width: 1200px; height: 960px; overflow: hidden;
    background: var(--backdrop);
    font-family: "Roboto", Arial, sans-serif;
  }
  .stage { position: relative; width: 1200px; height: 960px; }
  .card {
    position: absolute; width: 600px; height: 343px; overflow: hidden;
  }
  .card--front { left: 314px; top: 113px; background: var(--paper); }
  .card--back { left: 311px; top: 472px; background: var(--navy); }

  .brand {
    position: absolute; display: flex; align-items: center; gap: 12px;
    font-weight: 500; font-size: 38px; letter-spacing: 2px; line-height: 1;
  }
  .brand__square { width: 16px; height: 16px; background: var(--accent-red); flex: none; }
  .card--front .brand { left: 35px; top: 118px; color: var(--navy); }
  .card--back .brand { left: 32px; top: 232px; color: var(--white); }
  .card--back .brand__square { background: var(--white); }

  .address {
    position: absolute; left: 35px; top: 193px;
    font-size: 14px; line-height: 19px; color: var(--ink);
  }
  .contacts {
    position: absolute; left: 35px; top: 240px; list-style: none;
    font-size: 14px; line-height: 19px; color: var(--ink);
  }
  .contacts li { display: flex; align-items: center; gap: 9px; }
  .contacts svg { width: 13px; height: 13px; fill: var(--navy); flex: none; }

  .name-band {
    position: absolute; right: 0; top: 236px; width: 226px; height: 54px;
  }
  .name-band svg { position: absolute; inset: 0; }
  .name-band__text {
    position: absolute; right: 30px; top: 8px; text-align: center; color: var(--white);
  }
  .name-band__name { font-size: 19px; font-weight: 500; line-height: 22px; }
  .name-band__title { font-size: 14px; font-weight: 500; line-height: 18px; }

  .web {
    position: absolute; left: 33px; top: 302px;
    color: var(--white); font-size: 14px; letter-spacing: 4.4px;
  }
  .portrait {
    position: absolute; left: 340px; top: 16px; width: 250px; height: 327px;
    background: linear-gradient(180deg, var(--portrait-top), var(--portrait-bottom));
    border-radius: 90px 90px 0 0;
  }
</style>
</head>
<body>
<main class="stage">
  <section class="card card--front">
    <div class="brand"><span class="brand__square"></span>MERIDIAN</div>
    <p class="address">4120 Willow Crest Drive<br>Juneau, Alaska 34811</p>
    <ul class="contacts">
      <li><svg viewBox="0 0 24 24"><path d="M6.6 10.8a15 15 0 0 0 6.6 6.6l2.2-2.2a1 1 0 0 1 1-.25 11.4 11.4 0 0 0 3.6.57 1 1 0 0 1 1 1V20a1 1 0 0 1-1 1A17 17 0 0 1 3 4a1 1 0 0 1 1-1h3.5a1 1 0 0 1 1 1c0 1.25.2 2.45.57 3.57a1 1 0 0 1-.25 1z"/></svg>555 214 3860</li>
      <li><svg viewBox="0 0 24 24"><path d="M7 1h10a2 2 0 0 1 2 2v18a2 2 0 0 1-2 2H7a2 2 0 0 1-2-2V3a2 2 0 0 1 2-2zm0 3v14h10V4zm5 15.5a1 1 0 1 0 0 2 1 1 0 0 0 0-2z"/></svg>555 702 1947</li>
      <li><svg viewBox="0 0 24 24"><path d="M2 5h20v14H2zm2 2v.4l8 5 8-5V7l-8 5z"/></svg>daniel@meridianrealty.com</li>
      <li><svg viewBox="0 0 24 24"><path d="M12 2a10 10 0 1 0 0 20 10 10 0 0 0 0-20zm-1 17.9A8 8 0 0 1 4.2 10L9 15v1a2 2 0 0 0 2 2zm6.9-2.5A2 2 0 0 0 16 16h-1v-3a1 1 0 0 0-1-1H8v-2h2a1 1 0 0 0 1-1V7h2a2 2 0 0 0 2-2v-.4a8 8 0 0 1 2.9 12.8z"/></svg>www.meridianrealty.com</li>
    </ul>
    <div class="name-band">
      <svg viewBox="0 0 226 54" preserveAspectRatio="none"><polygon points="26,0 226,0 226,54 0,54" fill="var(--navy)"/></svg>
      <div class="name-band__text">
        <div class="name-band__name">DANIEL REYES</div>
        <div class="name-band__title">CEO/FOUNDER</div>
      </div>
    </div>
  </section>

  <section class="card card--back">
    <div class="brand"><span class="brand__square"></span>MERIDIAN</div>
    <p class="web">www.meridianrealty.com</p>
    <div class="portrait" role="img" aria-label="Portrait photo of the agent in a navy suit and striped tie"></div>
  </section>
</main>
</body>
</html>
```